Elegant Financial Planning Business Card

Clearpath Wealth Advisory Pty Ltd requires an elegant business card that communicates simplicity, elegance and trust.
Attached card example of 'Varnoth' is very close to what I am looking for. Looking for black and white card.
Update 24/1/16: The attached Varnoth card is almost exactly what I am looking for. Although it is possible that alternative layouts may interest me, it is considerably more likely that I will proceed with a virtual clone of the "Varnoth' example.
Industry/Entity Type
Financial Planning
Contact Information for Business Card
In black font...
Front Details are (layout as per Dana Varnoth card picture):
Line1 - Name: Oliver Marsh
Line 2 - Company: Clearpath Wealth Advisory Pty Ltd
Line 3 - Address: Harbourview Plaza 3, Level 17, 58 Lomond Avenue, Kestrel Bay VIC
Line 4
- Phone: 136 712
- Email: advice@cpwa-example.com.au
- Site: www.cpwa-example.com.au
Back details
1/ logo in position and dimensions as per attached layout
2. Bottom left (in smaller writing).
- Authorised Representative No. 517946
- Clearpath Wealth Advisory is a corporate authorised representative of Tarquay7 Capital Services Pty Ltd
- ABN 47 318 602 154
- AFSL No. 608139

```html
<!DOCTYPE html>
<html lang="en">
<head>
<meta charset="utf-8">
<title>Clearpath Wealth Advisory – Business Card</title>
<link rel="stylesheet" href="https://fonts.googleapis.com/css2?family=Tinos:wght@400;700&display=swap">
<style>
  :root {
    --backdrop: #3b3531;
    --card-white: #fbfbfa;
    --card-black: #1c1b1b;
    --ink: #1e1e1e;
    --ink-soft: #3a3a3a;
    --paper-text: #e9e9e9;
    --font-serif: "Tinos", "Times New Roman", serif;
  }
  * { box-sizing: border-box; margin: 0; padding: 0; }
  html, body { width: 1200px; height: 844px; overflow: hidden; }
  body {
    background: var(--backdrop);
    font-family: var(--font-serif);
    position: relative;
  }
  .card {
    position: absolute;
    top: 263px;
    width: 520px;
    height: 318px;
    border-radius: 3px;
    box-shadow: 0 10px 28px rgba(0,0,0,0.45);
  }
  .card--front { left: 60px; background: var(--card-white); color: var(--ink); }
  .card--back { left: 620px; background: var(--card-black); color: var(--paper-text); }

  .brand-name {
    position: absolute;
    right: 36px;
    text-align: right;
    font-weight: 400;
    line-height: 1.15;
    letter-spacing: 0.04em;
  }
  .card--front .brand-name { top: 60px; font-size: 19px; color: var(--ink); }
  .card--back .brand-name { top: 44px; font-size: 22px; color: #ffffff; }

  .holder {
    position: absolute;
    left: 40px;
    top: 150px;
  }
  .holder__name {
    font-size: 21px;
    font-weight: 700;
    margin-bottom: 10px;
  }
  .contact-list { list-style: none; font-size: 14px; color: var(--ink-soft); }
  .contact-list li { display: flex; align-items: center; gap: 10px; line-height: 20px; }
  .contact-list svg { width: 11px; height: 11px; flex: none; fill: var(--ink); }
  .address {
    margin-top: 8px;
    font-size: 15px;
    line-height: 20px;
    color: var(--ink-soft);
  }

  .compliance {
    position: absolute;
    left: 40px;
    bottom: 34px;
    font-size: 12.5px;
    line-height: 17px;
    color: var(--paper-text);
  }
  .compliance p + p { margin-top: 8px; }
</style>
</head>
<body>

  <section class="card card--front" aria-label="Business card front">
    <div class="brand-name">Clearpath Wealth<br>Advisory Pty Ltd</div>

    <div class="holder">
      <h1 class="holder__name">Oliver Marsh</h1>
      <ul class="contact-list">
        <li>
          <svg viewBox="0 0 12 12" aria-hidden="true"><path d="M2.5 0.8l2 2-1.1 1.4c.7 1.6 2 2.9 3.6 3.6l1.4-1.1 2 2-1.3 1.8C5 10.2 1.8 7 1.5 2.1z"/></svg>
          <span>136 712</span>
        </li>
        <li>
          <svg viewBox="0 0 12 12" aria-hidden="true"><path d="M0.5 2.5h11v7h-11z M1 3l5 3.6L11 3" stroke="#fbfbfa" stroke-width="0.9"/></svg>
          <span>advice@cpwa-example.com.au</span>
        </li>
        <li>
          <svg viewBox="0 0 12 12" aria-hidden="true"><circle cx="6" cy="6" r="5.5"/><path d="M0.5 6h11M6 0.5c-2.4 3-2.4 8 0 11M6 0.5c2.4 3 2.4 8 0 11" stroke="#fbfbfa" stroke-width="0.8" fill="none"/></svg>
          <span>www.cpwa-example.com.au</span>
        </li>
      </ul>
      <p class="address">Harbourview Plaza 3, Level 17, 58<br>Lomond Avenue, Kestrel Bay VIC</p>
    </div>
  </section>

  <section class="card card--back" aria-label="Business card back">
    <div class="brand-name">Clearpath Wealth<br>Advisory</div>

    <div class="compliance">
      <p>ABN 47 318 602 154<br>AFSL No. 608139</p>
      <p>Authorised Representative No. 517946</p>
      <p>Clearpath Wealth Advisory is a corporate authorised representative<br>of Tarquay7 Capital Services Pty Ltd</p>
    </div>
  </section>

</body>
</html>
```